Modern Catering Company needs Letterhead Design

We need a letterhead design that will make effective use of the corporate logo and color scheme, along with careful typography, helps this letterhead design communicate the brand well. We do have a corporate logo, however feel free to enhance the color scheme with gold and purple. We are serving a very upscale clientele so the letterhead has to reflect elegance, professionalism, cleanliness, and modern style. We are branding the company so the letterhead and business cards must fit the brand story. There should be no cartoonish elements in the design and we are looking for sharper lines.

Target Market(s)

Businesses and upscale clientele

Industry/Entity Type

Catering

Contact Information for Business Card

while this design can have any number of quirks and distinctions, it needs to be cohesive with the entire brand story clean, professional but edgy

Requirements
Must have
• must have good and carefully placement of it’s logo and where you place the text or the message. Colors blue, very deep purple, jewel tones not pastels, gold. Blue must be the primary color you may accent with purple or gold. Contact information is as follows: Co-Owners/ Chefs: R. Hollowell & T. Brenn, phone: 414-555-0182 email:Contact@emberoakcatering.example, address: 6172 W Larkmoor Ln, Milwaukee, WI 53299
Should not have
• pastel colors, Do not add the BBQ information to the letterhead or business card it was a mistake by the previous designer.

```html
<!DOCTYPE html>
<html lang="en">
<head>
<meta charset="utf-8">
<title>Ember Oak Catering – Stationery</title>
<link href="https://fonts.googleapis.com/css2?family=Questrial&display=swap" rel="stylesheet">
<style>
  :root {
    --backdrop: #cfcfd2;
    --paper: #f1f1f1;
    --ink: #2b2b2b;
    --brand-blue: #3a62dc;
    --charcoal: #2e2e30;
    --muted: #8c8c90;
  }
  * { box-sizing: border-box; margin: 0; padding: 0; }
  html, body { width: 1200px; height: 1069px; overflow: hidden; }
  body {
    background: var(--backdrop);
    font-family: "Questrial", "Century Gothic", sans-serif;
    color: var(--ink);
    position: relative;
  }

  /* Letterhead */
  .letterhead {
    position: absolute; left: 130px; top: 127px;
    width: 630px; height: 815px;
    background: var(--paper);
  }
  .wordmark {
    position: absolute; display: flex; align-items: center; gap: 8px;
    color: var(--brand-blue); text-transform: uppercase; line-height: 1.1;
  }
  .wordmark-dot { border-radius: 50%; background: var(--brand-blue); flex: none; }
  .letterhead .wordmark { left: 56px; top: 78px; font-size: 22px; letter-spacing: 2px; }
  .letterhead .wordmark-dot { width: 16px; height: 16px; }

  .contact-block {
    position: absolute; left: 442px; top: 50px;
    font-size: 8.6px; line-height: 11.2px;
  }
  .contact-line { display: flex; align-items: center; gap: 6px; }
  .contact-icon { width: 8px; height: 8px; flex: none; }
  .contact-address { margin-top: 8px; }

  .letter-body {
    position: absolute; left: 57px; top: 256px; width: 516px;
    font-size: 9.6px; line-height: 11.2px; text-align: justify;
  }
  .letter-body p { margin-bottom: 11px; }
  .salutation { font-weight: bold; margin-bottom: 12px !important; }
  .sign-off { position: absolute; left: 57px; top: 525px; font-size: 9.6px; line-height: 11.5px; }
  .sign-off strong { display: block; }
  .signature {
    position: absolute; left: 127px; top: 508px; width: 132px; height: 70px;
    background: linear-gradient(90deg, #e6e8f3, #dfe2f2);
  }
  .band { position: absolute; left: 0; bottom: 0; width: 100%; }

  /* Business cards */
  .card { position: absolute; left: 810px; width: 261px; height: 149px; background: var(--paper); }
  .card-front { top: 272px; }
  .card-dark { top: 461px; background: var(--charcoal); }
  .card-light { top: 650px; }
  .card-front .wordmark { left: 18px; top: 58px; font-size: 13px; letter-spacing: 1px; gap: 5px; }
  .card-front .wordmark-dot { width: 9px; height: 9px; }
  .card-divider { position: absolute; left: 125px; top: 42px; width: 1px; height: 64px; background: #c9c9cc; }
  .card-details { position: absolute; left: 143px; top: 38px; font-size: 6.4px; line-height: 8.4px; }
  .card-name { color: var(--brand-blue); font-weight: bold; font-size: 7px; letter-spacing: .3px; }
  .card-role { color: #555; margin-bottom: 7px; }
  .card-details .contact-icon { width: 6px; height: 6px; }
  .card-details .contact-line { gap: 4px; }
  .card-details .contact-address { margin-top: 5px; }
  .centered-mark {
    left: 0; right: 0; top: 52px; justify-content: center;
    font-size: 16px; letter-spacing: 1.5px; gap: 6px;
  }
  .centered-mark .wordmark-dot { width: 10px; height: 10px; }
  .card-url {
    position: absolute; left: 0; right: 0; top: 124px;
    text-align: center; font-size: 6.4px;
  }
  .card-dark .card-url { top: 124px; color: var(--muted); }
  .card-light .card-url { top: 124px; color: #555; }
</style>
</head>
<body>

<section class="letterhead">
  <div class="wordmark"><span class="wordmark-dot"></span><span>Ember Oak<br>Catering</span></div>

  <div class="contact-block">
    <div class="contact-line">
      <svg class="contact-icon" viewBox="0 0 8 8"><rect width="8" height="8" rx="1.5" fill="#3a62dc"/><path d="M2.3 1.8l1 1-.6.7c.4.8 1 1.3 1.7 1.7l.6-.6 1 1-.8.8C3.5 6.2 1.8 4.5 1.6 2.6z" fill="#fff"/></svg>
      <span>+1 414-555-0182</span>
    </div>
    <div class="contact-line">
      <svg class="contact-icon" viewBox="0 0 8 8"><rect width="8" height="8" rx="1.5" fill="#3a62dc"/><rect x="1.6" y="2.3" width="4.8" height="3.4" fill="none" stroke="#fff" stroke-width=".7"/><path d="M1.6 2.3L4 4.2l2.4-1.9" fill="none" stroke="#fff" stroke-width=".7"/></svg>
      <span>info@emberoakcatering.example</span>
    </div>
    <div class="contact-line">
      <svg class="contact-icon" viewBox="0 0 8 8"><rect width="8" height="8" rx="1.5" fill="#3a62dc"/><circle cx="4" cy="4" r="2.4" fill="none" stroke="#fff" stroke-width=".6"/><path d="M1.6 4h4.8M4 1.6v4.8" stroke="#fff" stroke-width=".5"/></svg>
      <span>www.emberoakcatering.example</span>
    </div>
    <div class="contact-address">6172 W Larkmoor Ln<br>Milwaukee, WI 53299</div>
  </div>

  <div class="letter-body">
    <p class="salutation">Dear sir,</p>
    <p>Communication is a very integral part of living creatures, animals and humans. Communication may be verbal or written. Written communication however is only applicable to human beings. Can you even imagine a world without communication? Verbal communication can be through telephones, webcams or in person. Written communication is through letters, emails and mobile phone messages.</p>
    <p>In today’s world of great inventions and technology, letters have somehow become redundant. It is the time for text messages or chats. But they still can communicate a lot more than all other modes of communication. Organizations and various government departments still bank on letters as a strong medium of communication. There is no comparison in costs of sending letters as compared to costs of mobile phone messages though – letters are far cheaper. Letters now commonly known as “hard copy documents” are considered more relevant and important than email copies of text messages as proof or evidence of some sort.</p>
    <p>Letters speak volumes about a person or an organization that writes it. So one must take utmost care ensuring that the language used in any letter is appropriate for the occasion for which it is being written. Since a letter is also a written proof or document, if there are certain things that should not form a part of it, then that too should be carefully handled.</p>
    <p>Writing a good letter is an art. But if for some reason someone is unable to write that perfect letter, these different types of letters provide a base for you to build on. Sample letters have been given for everyone to understand what all information needs to form a part of the letter type and then it can be customized.</p>
  </div>

  <div class="sign-off">Yours Sincerely,<strong>Corin Vale</strong></div>
  <div class="signature" role="img" aria-label="Handwritten signature in blue ink"></div>

  <svg class="band" width="630" height="10" viewBox="0 0 630 10" preserveAspectRatio="none">
    <polygon points="0,0 414,0 406,10 0,10" fill="#2e2e30"/>
    <polygon points="419,0 630,0 630,10 411,10" fill="#3a62dc"/>
  </svg>
</section>

<section class="card card-front">
  <div class="wordmark"><span class="wordmark-dot"></span><span>Ember Oak<br>Catering</span></div>
  <div class="card-divider"></div>
  <div class="card-details">
    <div class="card-name">JORDAN PELL</div>
    <div class="card-role">General Manager</div>
    <div class="contact-line">
      <svg class="contact-icon" viewBox="0 0 8 8"><rect width="8" height="8" rx="1.5" fill="#3a62dc"/><path d="M2.3 1.8l1 1-.6.7c.4.8 1 1.3 1.7 1.7l.6-.6 1 1-.8.8C3.5 6.2 1.8 4.5 1.6 2.6z" fill="#fff"/></svg>
      <span>+1 414-555-0182</span>
    </div>
    <div class="contact-line">
      <svg class="contact-icon" viewBox="0 0 8 8"><rect width="8" height="8" rx="1.5" fill="#3a62dc"/><rect x="1.6" y="2.3" width="4.8" height="3.4" fill="none" stroke="#fff" stroke-width=".7"/></svg>
      <span>info@emberoakcatering.example</span>
    </div>
    <div class="contact-line">
      <svg class="contact-icon" viewBox="0 0 8 8"><rect width="8" height="8" rx="1.5" fill="#3a62dc"/><circle cx="4" cy="4" r="2.4" fill="none" stroke="#fff" stroke-width=".6"/></svg>
      <span>www.emberoakcatering.example</span>
    </div>
    <div class="contact-address">6172 W Larkmoor Ln<br>Milwaukee, WI 53299</div>
  </div>
  <svg class="band" width="261" height="6" viewBox="0 0 261 6" preserveAspectRatio="none">
    <polygon points="0,0 124,0 120,6 0,6" fill="#2e2e30"/>
    <polygon points="127,0 261,0 261,6 123,6" fill="#3a62dc"/>
  </svg>
</section>

<section class="card card-dark">
  <div class="wordmark centered-mark"><span class="wordmark-dot"></span><span>Ember Oak<br>Catering</span></div>
  <div class="card-url">www.emberoakcatering.example</div>
</section>

<section class="card card-light">
  <div class="wordmark centered-mark"><span class="wordmark-dot"></span><span>Ember Oak<br>Catering</span></div>
  <div class="card-url">www.emberoakcatering.example</div>
</section>

</body>
</html>
```